디자인 카테고리
로고+명함 (IT/미디어 업종)
브랜드 소개
본 브랜드는 국내 개별여행자들에게 보다 쉽고 간편하게 여행지에 대한 할인혜택과 정보를 받을 수 있는 020 서비스플랫폼임.
모두로 [ M-DURO]는 전국 유료여행지와 상호 제휴하여 고객이 미리 결제하지 않고 현장에서 등록되어있는 자신의 모바일앱(소비자 무료가입)을 통해 할인된 금액으로 손쉽게 여행상품을 후결제 이용할 수 있는 신개념 여행플랫폼 서비스이다.
여행자는 여행정보를 손쉽게 얻을 수 있을뿐만 아니라 주변여행지 검색까지 가능하며 관광지 운영자는 다양한 온라인 마케팅기회가 주어지며 주변관광지와의 시너지 효과를 통해 매출증대가 가능함
차후 외국어버전을 통해 외국인이 한국을 방문하여 여행을 할때에도 사용가능토록 업그레이드 예정임.

```html
<!DOCTYPE html>
<html lang="ko">
<head>
<meta charset="utf-8">
<title>모두로 명함</title>
<link href="https://fonts.googleapis.com/css2?family=Nanum+Gothic:wght@400;700;800&display=swap" rel="stylesheet">
<style>
  :root {
    --backdrop: #e7e5e2;
    --card: #fbfaf8;
    --ink: #3b4048;
    --ink-soft: #5a5f66;
    --accent: #e85a1c;
    --ghost: #ecebe8;
    --rule: #4a4f56;
  }
  * { margin: 0; padding: 0; box-sizing: border-box; }
  html, body {
    width: 1200px; height: 1200px; overflow: hidden;
    background: var(--backdrop);
    font-family: "Nanum Gothic", sans-serif;
    color: var(--ink);
  }
  .card {
    position: absolute;
    left: 100px; top: 320px;
    width: 1000px; height: 560px;
    background: var(--card);
    box-shadow: 0 12px 30px rgba(0,0,0,0.12);
    overflow: hidden;
  }
  .ghost-circle {
    position: absolute;
    left: 560px; top: -10px;
    width: 400px; height: 400px;
    border-radius: 50%;
    background: var(--ghost);
  }
  .brand {
    position: absolute;
    left: 70px; top: 150px;
    display: flex; align-items: center; gap: 30px;
  }
  .brand-dot {
    width: 112px; height: 112px; border-radius: 50%;
    background: var(--accent);
  }
  .brand-name {
    font-weight: 800; font-size: 92px; letter-spacing: 4px;
    line-height: 1; color: var(--ink);
  }
  .tagline {
    position: absolute;
    left: 212px; top: 262px;
    font-size: 17px; font-weight: 700; color: var(--ink);
    letter-spacing: 0.5px;
  }
  .person {
    position: absolute;
    right: 440px; top: 330px;
    text-align: right;
  }
  .person-role { font-size: 22px; letter-spacing: 10px; color: var(--ink-soft); }
  .person-name { font-size: 40px; letter-spacing: 12px; margin-top: 10px; color: var(--ink); }
  .divider {
    position: absolute;
    left: 584px; top: 326px;
    width: 2px; height: 190px;
    background: var(--rule);
  }
  .contacts {
    position: absolute;
    left: 604px; top: 326px;
    list-style: none;
    font-size: 22px; line-height: 38px; color: var(--ink);
  }
  .contacts .label { color: var(--accent); display: inline-block; width: 30px; }
  .contacts .indent { padding-left: 30px; }
</style>
</head>
<body>
  <div class="card">
    <div class="ghost-circle"></div>
    <div class="brand">
      <div class="brand-dot"></div>
      <div class="brand-name">M-DURO</div>
    </div>
    <div class="tagline">국내 개별여행 플랫폼 서비스- 모두로</div>
    <div class="person">
      <div class="person-role">대표</div>
      <div class="person-name">서지안</div>
    </div>
    <div class="divider"></div>
    <ul class="contacts">
      <li><span class="label">A.</span>서울시 마포구 연남동</li>
      <li class="indent">OO빌딩 9층</li>
      <li><span class="label">C.</span>010-5820-3147</li>
      <li><span class="label">F.</span>02-555-0183</li>
      <li><span class="label">M.</span>hello@moduro.kr</li>
    </ul>
  </div>
</body>
</html>
```